Business Card Design for a Lending Business (Hard Money loans)

We need a business card for our Real Estate Lending business. We do hard Money loans for real estate investors. We have an existing logo we like, see attached. I'd like the business card to mostly include the logo colors, but a bright color pop of some sort would be nice to see also. Card should include Logo, Company Name, Company Address, Employee Name, Cell Phone, Main Phone, Email, Website

Industry/Entity Type

Finance / Lending

Contact Information for Business Card

Logo, Company Name, Company Address, Employee Name, Cell Phone, Main Phone, Email, Website

Requirements
Nice to have
• I'd like the business card to mostly include the logo colors, but a bright color pop of some sort would be nice to see also.

```html
<!DOCTYPE html>
<html lang="en">
<head>
<meta charset="UTF-8">
<title>Harborline Lending – Business Card</title>
<link href="https://fonts.googleapis.com/css2?family=Montserrat:wght@500;600;700;800&display=swap" rel="stylesheet">
<style>
  :root {
    --navy: #2b3781;
    --navy-deep: #232d6e;
    --cyan: #00afe0;
    --white: #ffffff;
    --silver: #c9ccd6;
    --stage: #76757b;
    --ink-faint: rgba(255,255,255,0.07);
  }
  * { margin: 0; padding: 0; box-sizing: border-box; }
  html, body {
    width: 1200px; height: 900px; overflow: hidden;
    background: var(--stage);
    font-family: "Montserrat", sans-serif;
  }
  .canvas { position: relative; width: 1200px; height: 900px; }

  .card {
    position: absolute;
    width: 700px; height: 400px;
    border-radius: 18px;
    overflow: hidden;
    box-shadow: 0 8px 22px rgba(0,0,0,0.35);
  }
  .card--front { left: 250px; top: 40px; background: var(--white); }
  .card--back  { left: 250px; top: 460px; background: var(--navy); }

  /* Front */
  .front-mark {
    position: absolute; right: 60px; top: 50px;
    width: 260px; height: 260px; border-radius: 50%;
    background: var(--navy);
  }
  .wordmark { position: absolute; }
  .wordmark__name {
    font-weight: 800; letter-spacing: 4px; line-height: 1;
  }
  .wordmark__sub {
    display: flex; align-items: center; gap: 10px;
    font-weight: 600; letter-spacing: 7px;
  }
  .wordmark__rule { height: 2px; flex: 1; }

  .front-wordmark { left: 44px; top: 52px; width: 320px; }
  .front-wordmark .wordmark__name { font-size: 34px; color: var(--navy); }
  .front-wordmark .wordmark__sub { font-size: 13px; color: var(--cyan); margin-top: 8px; }
  .front-wordmark .wordmark__rule { background: var(--cyan); }

  .person { position: absolute; left: 44px; top: 150px; }
  .person__name { font-size: 20px; font-weight: 800; color: var(--navy); letter-spacing: 0.5px; }
  .person__title { font-size: 14px; font-weight: 600; color: var(--cyan); margin-top: 2px; }

  .contact-list { list-style: none; position: absolute; left: 44px; top: 218px; }
  .contact-list li {
    display: flex; align-items: center; gap: 10px;
    font-size: 14px; font-weight: 500; color: var(--navy);
    height: 24px;
  }
  .contact-list svg { width: 14px; height: 14px; flex: none; }
  .address { position: absolute; left: 44px; top: 330px; font-size: 14px; font-weight: 500; color: var(--navy); line-height: 22px; }

  /* Back */
  .back-deco {
    position: absolute; right: -90px; top: -40px;
    width: 420px; height: 420px; border-radius: 50%;
    background: var(--ink-faint);
  }
  .back-wordmark { left: 50%; top: 50%; transform: translate(-50%, -50%); width: 360px; }
  .back-wordmark .wordmark__name { font-size: 40px; color: var(--silver); text-align: center; }
  .back-wordmark .wordmark__sub { font-size: 14px; color: var(--silver); margin-top: 10px; }
  .back-wordmark .wordmark__rule { background: var(--silver); }
</style>
</head>
<body>
<main class="canvas">

  <section class="card card--front" aria-label="Business card front">
    <div class="wordmark front-wordmark">
      <div class="wordmark__name">HARBORLINE</div>
      <div class="wordmark__sub"><span class="wordmark__rule"></span>LENDING<span class="wordmark__rule"></span></div>
    </div>

    <div class="person">
      <div class="person__name">DANIEL REYES</div>
      <div class="person__title">CEO/FOUNDER</div>
    </div>

    <ul class="contact-list">
      <li>
        <svg viewBox="0 0 24 24" fill="var(--cyan)"><path d="M6.6 10.8a15.1 15.1 0 0 0 6.6 6.6l2.2-2.2c.3-.3.7-.4 1-.2 1.1.4 2.3.6 3.6.6.6 0 1 .4 1 1V20c0 .6-.4 1-1 1A17 17 0 0 1 3 4c0-.6.4-1 1-1h3.5c.6 0 1 .4 1 1 0 1.3.2 2.5.6 3.6.1.3 0 .7-.2 1z"/></svg>
        312 555 0147
      </li>
      <li>
        <svg viewBox="0 0 24 24" fill="none" stroke="var(--cyan)" stroke-width="2.4"><rect x="6" y="2" width="12" height="20" rx="2"/><line x1="10" y1="18" x2="14" y2="18"/></svg>
        312 555 0198
      </li>
      <li>
        <svg viewBox="0 0 24 24" fill="var(--cyan)"><path d="M2 5h20v14H2z" opacity=".9"/><path d="M2 5l10 8 10-8" fill="none" stroke="#fff" stroke-width="2"/></svg>
        daniel@harborlinelending.com
      </li>
      <li>
        <svg viewBox="0 0 24 24" fill="none" stroke="var(--cyan)" stroke-width="2"><circle cx="12" cy="12" r="10"/><ellipse cx="12" cy="12" rx="4" ry="10"/><line x1="2" y1="12" x2="22" y2="12"/></svg>
        www.harborlinelending.com
      </li>
    </ul>

    <address class="address" style="font-style:normal">
      418 Lakeview Drive, Suite 210<br>Riverton, MI 49012
    </address>

    <div class="front-mark" aria-hidden="true"></div>
  </section>

  <section class="card card--back" aria-label="Business card back">
    <div class="back-deco" aria-hidden="true"></div>
    <div class="wordmark back-wordmark">
      <div class="wordmark__name">HARBORLINE</div>
      <div class="wordmark__sub"><span class="wordmark__rule"></span>LENDING<span class="wordmark__rule"></span></div>
    </div>
  </section>

</main>
</body>
</html>
```